Tallow Bright business card

Tallow Bright is a new online life insurance company providing instant quotes and policies to consumers.
Target Market(s)
Target market is both business to business as well as business to consumer
Can think out side of the box- We are an open minded bunch
Industry/Entity Type
Life Insurance
Requirements
Must have
- Our corporate Logo
Double sided
Website www.tallowbright.com.au
Phone Number
Name & Position of each person etc.
Modern font

```html
<!DOCTYPE html>
<html lang="en">
<head>
<meta charset="utf-8">
<title>Tallow Bright business card</title>
<link rel="stylesheet" href="https://fonts.googleapis.com/css2?family=Arimo:wght@400;700&display=swap">
<style>
  :root {
    --page: #ffffff;
    --card: #cfcfcf;
    --wave: #ddd3b8;
    --ink: #1c1c1c;
    --accent: #f5821f;
    --light: #ffffff;
    --rule: #8a8a8a;
  }
  * { box-sizing: border-box; margin: 0; padding: 0; }
  html, body {
    width: 916px; height: 1200px; overflow: hidden;
    background: var(--page);
    font-family: "Arimo", Arial, sans-serif;
  }
  .sheet { position: relative; width: 916px; height: 1200px; }
  .card {
    position: absolute; left: 54px; width: 807px; height: 459px;
    background: var(--card); overflow: hidden;
  }
  .card--front { top: 114px; }
  .card--back { top: 630px; }
  .wave-pattern { position: absolute; inset: 0; }

  .brand {
    position: absolute; display: flex; align-items: center;
    color: var(--ink); font-weight: 700; white-space: nowrap;
  }
  .brand__dot { border-radius: 50%; background: var(--accent); flex: none; }
  .card--front .brand {
    left: 0; right: 0; top: 130px; justify-content: center;
    font-size: 78px; letter-spacing: -1px; gap: 18px;
  }
  .card--front .brand__dot { width: 30px; height: 30px; }
  .card--back .brand {
    left: 0; width: 380px; top: 150px; justify-content: center;
    font-size: 38px; letter-spacing: -0.5px; gap: 10px;
  }
  .card--back .brand__dot { width: 15px; height: 15px; }

  .website { position: absolute; color: var(--light); text-align: center; }
  .card--front .website { left: 0; right: 0; top: 330px; font-size: 22px; }
  .card--back .website {
    left: 0; width: 380px; top: 281px; font-size: 22px;
    text-shadow: 1px 2px 3px rgba(0,0,0,0.55);
  }

  .divider {
    position: absolute; left: 380px; top: 33px; width: 1px; height: 400px;
    background: var(--rule);
  }
  .contact { position: absolute; left: 401px; top: 113px; color: var(--ink); font-size: 22px; line-height: 30px; }
  .contact__name { color: var(--accent); font-weight: 700; font-size: 27px; line-height: 34px; text-shadow: 1px 1px 2px rgba(0,0,0,0.25); }
  .contact__role { margin-bottom: 34px; }
  .contact__phone { margin-top: 16px; }
</style>
</head>
<body>
<div class="sheet">
  <section class="card card--front">
    <svg class="wave-pattern" width="807" height="459" role="img" aria-label="Faint dotted wave pattern sweeping across the card">
      <defs>
        <linearGradient id="waveFront" x1="0" y1="1" x2="1" y2="0">
          <stop offset="0" stop-color="var(--wave)" stop-opacity="0"/>
          <stop offset="0.5" stop-color="var(--wave)" stop-opacity="0.55"/>
          <stop offset="1" stop-color="var(--wave)" stop-opacity="0.2"/>
        </linearGradient>
      </defs>
      <path d="M90 459 C260 200 520 120 807 0 L807 140 C580 220 340 330 250 459 Z" fill="url(#waveFront)"/>
    </svg>
    <div class="brand"><span class="brand__name">Tallow Bright</span><span class="brand__dot"></span></div>
    <p class="website">www.tallowbright.com.au</p>
  </section>

  <section class="card card--back">
    <svg class="wave-pattern" width="807" height="459" role="img" aria-label="Faint dotted wave pattern sweeping across the card">
      <defs>
        <linearGradient id="waveBack" x1="0" y1="0" x2="1" y2="1">
          <stop offset="0" stop-color="var(--wave)" stop-opacity="0.5"/>
          <stop offset="0.6" stop-color="var(--wave)" stop-opacity="0.15"/>
          <stop offset="1" stop-color="var(--wave)" stop-opacity="0.45"/>
        </linearGradient>
      </defs>
      <path d="M0 20 C200 120 420 260 807 280 L807 459 L560 459 C420 380 200 260 0 220 Z" fill="url(#waveBack)"/>
      <path d="M520 459 C620 300 700 120 807 0 L807 180 C740 280 680 380 650 459 Z" fill="url(#waveBack)"/>
    </svg>
    <div class="brand"><span class="brand__name">Tallow Bright</span><span class="brand__dot"></span></div>
    <p class="website">www.tallowbright.com.au</p>
    <div class="divider"></div>
    <div class="contact">
      <p class="contact__name">ELLA MOSS</p>
      <p class="contact__role">Manager</p>
      <p class="contact__address">Level 18, 42 Harbour Lane<br>Northbay NSW 2061</p>
      <p class="contact__phone">+0198765432</p>
    </div>
  </section>
</div>
</body>
</html>
```